I am a home builder and developer

I would like some sort of architectural design like a pencil type of drawing of a house but want it to be professional looking and two sided.

Simply I am a custom home builder and land developer. I would like a new design other than what I have now that's what I thought y'all did. I like mostly black maybe with an pencil type of drawing of a house. Like an architectural look.

Industry/Entity Type

Home Builder

```html
<!DOCTYPE html>
<html lang="en">
<head>
<meta charset="UTF-8">
<title>Crestline Homes Inc — Business Card</title>
<link rel="stylesheet" href="https://fonts.googleapis.com/css2?family=Oswald:wght@500;600&family=Open+Sans:wght@400;600&display=swap">
<style>
  :root {
    --backdrop-light: #8f8f8f;
    --backdrop-dark: #4a4a4a;
    --card: #1d1d1e;
    --card-edge: #262627;
    --silver: #c9cacc;
    --white: #f4f4f4;
    --muted: #b9babc;
    --accent: #2e9fdc;
    --divider: #5a5a5c;
  }
  * { box-sizing: border-box; margin: 0; padding: 0; }
  html, body {
    width: 1200px;
    height: 1000px;
    overflow: hidden;
  }
  body {
    position: relative;
    background: radial-gradient(ellipse at 45% 30%, var(--backdrop-light) 0%, var(--backdrop-dark) 100%);
    font-family: "Open Sans", sans-serif;
  }
  .card {
    position: absolute;
    width: 540px;
    height: 310px;
    border-radius: 30px;
    background: linear-gradient(160deg, var(--card-edge), var(--card));
    box-shadow: 0 18px 40px rgba(0, 0, 0, 0.45);
  }
  .card--front { left: 100px; top: 140px; }
  .card--back { left: 560px; top: 550px; }

  /* Front */
  .brand {
    position: absolute;
    inset: 0;
    display: flex;
    align-items: center;
    justify-content: center;
    gap: 14px;
  }
  .brand__mark {
    width: 18px;
    height: 18px;
    background: var(--silver);
  }
  .brand__name {
    font-family: "Oswald", sans-serif;
    font-weight: 600;
    font-size: 38px;
    letter-spacing: 1px;
    color: var(--silver);
    text-transform: uppercase;
  }

  /* Back */
  .identity {
    position: absolute;
    right: 300px;
    top: 108px;
    text-align: right;
  }
  .identity__name {
    font-family: "Oswald", sans-serif;
    font-weight: 600;
    font-size: 30px;
    line-height: 1.1;
    color: var(--white);
    text-transform: uppercase;
  }
  .identity__role {
    font-size: 16px;
    font-weight: 600;
    color: var(--accent);
    margin-top: 2px;
  }
  .divider {
    position: absolute;
    left: 258px;
    top: 96px;
    width: 1px;
    height: 80px;
    background: var(--divider);
  }
  .contacts {
    position: absolute;
    left: 276px;
    top: 98px;
    list-style: none;
  }
  .contacts__item {
    display: flex;
    align-items: center;
    gap: 12px;
    font-size: 14px;
    line-height: 26px;
    color: var(--muted);
  }
  .contacts__item svg { width: 12px; height: 12px; fill: var(--accent); flex: none; }
  .contacts__highlight { color: var(--accent); }
  .address {
    position: absolute;
    left: 0;
    right: 0;
    bottom: 52px;
    display: flex;
    align-items: center;
    justify-content: center;
    gap: 8px;
    font-size: 14px;
    color: var(--muted);
  }
  .address svg { width: 12px; height: 15px; fill: var(--accent); }
</style>
</head>
<body>
  <section class="card card--front" aria-label="Card front">
    <div class="brand">
      <span class="brand__mark"></span>
      <span class="brand__name">Crestline Homes Inc</span>
    </div>
  </section>

  <section class="card card--back" aria-label="Card back">
    <div class="identity">
      <p class="identity__name">Owen Hartley</p>
      <p class="identity__role">Chief Engineer</p>
    </div>
    <div class="divider"></div>
    <ul class="contacts">
      <li class="contacts__item">
        <svg viewBox="0 0 24 24" aria-hidden="true"><path d="M6.6 10.8a15.1 15.1 0 0 0 6.6 6.6l2.2-2.2c.3-.3.7-.4 1-.2 1.1.4 2.3.6 3.6.6.6 0 1 .4 1 1V20c0 .6-.4 1-1 1A17 17 0 0 1 3 4c0-.6.4-1 1-1h3.5c.6 0 1 .4 1 1 0 1.3.2 2.5.6 3.6.1.3 0 .7-.2 1z"/></svg>
        555-014-2290
      </li>
      <li class="contacts__item">
        <svg viewBox="0 0 24 24" aria-hidden="true"><path d="M2 5h20v14H2zm2 2v.4l8 5 8-5V7zm0 2.8V17h16V9.8l-8 5z"/></svg>
        hello@crestlinehomes.com
      </li>
      <li class="contacts__item">
        <svg viewBox="0 0 24 24" aria-hidden="true"><path d="M12 2a10 10 0 1 0 0 20 10 10 0 0 0 0-20zm6.9 6h-3a15 15 0 0 0-1.3-3.9A8 8 0 0 1 18.9 8zM12 4c.8 1.2 1.5 2.5 1.9 4h-3.8c.4-1.5 1.1-2.8 1.9-4zM4.3 14a8 8 0 0 1 0-4h3.4a16 16 0 0 0 0 4zm.8 2h3a15 15 0 0 0 1.3 3.9A8 8 0 0 1 5.1 16zm3-8h-3a8 8 0 0 1 4.3-3.9C8.8 5.3 8.4 6.6 8.1 8zM12 20c-.8-1.2-1.5-2.5-1.9-4h3.8c-.4 1.5-1.1 2.8-1.9 4zm2.3-6H9.7a14 14 0 0 1 0-4h4.6a14 14 0 0 1 0 4zm.3 5.9c.6-1.2 1-2.5 1.3-3.9h3a8 8 0 0 1-4.3 3.9zm1.7-5.9a16 16 0 0 0 0-4h3.4a8 8 0 0 1 0 4z"/></svg>
        <span>www.<span class="contacts__highlight">crestlinehomes</span>.com</span>
      </li>
    </ul>
    <p class="address">
      <svg viewBox="0 0 24 30" aria-hidden="true"><path d="M12 0a11 11 0 0 0-11 11c0 8 11 19 11 19s11-11 11-19A11 11 0 0 0 12 0zm0 15a4 4 0 1 1 0-8 4 4 0 0 1 0 8z"/></svg>
      Your Street Address, Ridgefield, 1234
    </p>
  </section>
</body>
</html>
```